PostCard Design Project

I am making a mailing postcard
I am having the mailing printed using 4 color foil on certain parts.
I am looking for a design that maximizes the foil process where certain parts are done in foil to grab the customers attention (example: if there is a car on the postcard the headlights would be done in foil) .
I am targeting some industries, (auto, real estate, medical, beauty) I would like the post card to have examples of postcard ideas for 2 or 3 of these industries.
specs:
the postcard should be atleast 6.5x9 up to 8.5x11, I don't want to restrict the space for the creative as I don't want everything to look like a huge mess. both sides will be used.
the piece is a direct mail piece so it has to meet requirements of https://www.parcelvane-post.com/business/pdf/quick-reference-guide.pdf
text will be
"business with no limits, meet mailing with no addresses, gain new customers through "Whole Route Flyer Drop" reach new customers at their home without needing their address. "
I also want some current print specials I am running included.
-double your order FREE (order 500 business cards and get 1000)
-250 100lb gloss stock brochures 99.00
-business packages (cards, envelopes and letterhead) 299
-1000 flyers 140.40
-5000 postcards 179.99
A list of services
banners
booklets
brochures
business cards
calendars
catalogs
CD/DVD packages
envelopes
event tickets
flyers
hangtags
postcards
posters
presentation folders
rack cards
labels
table tents
window cling and decal
"order 24/7 orders@cardwillow.com" must be included
my logo is CardWillow will be supplied later
ive received some great designs. however Im looking for something a little more modern like some zelkor would put out. if the amount of words is too much please feel free to edit. also an idea i had for the list of services i offer is to have it transparent yet readable as the background of the postcard some small some big but covering the entire backgroud. you can then design on top of that with other thing. just an early morning thought
Reason: I have uploaded a sketch of my idea, please take time to look at it for an accurate depiction of what im looking for. feel free to add elements that make it pop off the page
Reason: We are getting close i will be providing feed back today
Business

```html
<!DOCTYPE html>
<html lang="en">
<head>
<meta charset="utf-8">
<title>CardWillow – Direct Mail Postcard</title>
<link rel="stylesheet" href="https://fonts.googleapis.com/css2?family=Open+Sans:wght@400;600;700;800&family=Oswald:wght@500;700&display=swap">
<style>
  :root {
    --paper: #ffffff;
    --ink: #1f1f1f;
    --night: #231f20;
    --red: #c8202f;
    --orange: #f39a1e;
    --grey: #7d7d7d;
    --lime: #d6e12a;
    --sky: #1ba9e6;
    --scarlet: #ec1c24;
    --amber: #f7ad3c;
    --ghost: rgba(255,255,255,0.14);
  }
  * { box-sizing: border-box; margin: 0; padding: 0; }
  html, body { width: 963px; height: 1200px; overflow: hidden; background: var(--paper); }
  .postcard { position: relative; width: 963px; height: 1200px; background: var(--paper); font-family: "Open Sans", Arial, sans-serif; color: var(--ink); }

  .headline { position: absolute; left: 69px; top: 52px; font-size: 60px; font-weight: 600; letter-spacing: 0.5px; white-space: nowrap; }
  .shine { position: absolute; left: 66px; top: 110px; font-family: "Oswald", Impact, sans-serif; font-weight: 700; font-size: 150px; line-height: 1; color: var(--red); letter-spacing: 2px; }
  .hours, .email { position: absolute; left: 69px; font-family: "Oswald", Impact, sans-serif; font-weight: 500; color: var(--orange); white-space: nowrap; line-height: 1; }
  .hours { top: 292px; font-size: 48px; }
  .email { top: 358px; font-size: 46px; }

  .brand { position: absolute; left: 622px; top: 184px; display: flex; align-items: center; gap: 12px; font-weight: 700; font-size: 46px; color: var(--grey); line-height: 1; }
  .brand-mark { width: 28px; height: 28px; background: var(--grey); }

  .photo { position: absolute; border: 7px solid var(--red); border-radius: 18px; overflow: hidden; }
  .photo--dental { left: 621px; top: 235px; width: 291px; height: 182px; background: linear-gradient(135deg, #e9d9cf, #9a8578 60%, #3e3a38); }
  .photo--beauty { left: 275px; top: 404px; width: 294px; height: 191px; background: linear-gradient(120deg, #cfd9df, #e6cdbf 55%, #f3efec); }
  .photo--auto { left: 592px; top: 436px; width: 368px; height: 270px; background: linear-gradient(160deg, #e0262f, #9c1118 55%, #2a2a2a); z-index: 2; }
  .photo-tag { position: absolute; right: 12px; bottom: 4px; font-weight: 700; font-size: 28px; color: #e5d23a; letter-spacing: 1px; }

  .night-band { position: absolute; left: 0; top: 597px; width: 963px; height: 593px; background: var(--night); }

  .ghost-words { position: absolute; left: 0; top: 597px; width: 963px; height: 593px; overflow: hidden; }
  .ghost-words span { position: absolute; color: var(--ghost); font-weight: 600; font-size: 20px; white-space: nowrap; }

  .services-title { position: absolute; left: 74px; top: 558px; font-size: 46px; font-weight: 600; letter-spacing: 1px; z-index: 3; }
  .services-title span:nth-child(1){color:#1a1a1a}.services-title span:nth-child(2){color:#e8308a}
  .services-title span:nth-child(3){color:#f39a1e}.services-title span:nth-child(4){color:#8cc63f}
  .services-title span:nth-child(5){color:#1ba9e6}.services-title span:nth-child(6){color:#ec1c24}
  .services-title span:nth-child(7){color:#f7d117}.services-title span:nth-child(8){color:#7a4aa0}

  .service-list { position: absolute; left: 84px; top: 642px; list-style: none; }
  .service-list li { position: relative; padding-left: 17px; height: 31px; font-size: 20px; line-height: 31px; color: #fff; white-space: nowrap; }
  .service-list li::before { content: ""; position: absolute; left: 0; top: 12px; width: 7px; height: 7px; border-radius: 50%; background: var(--dot); }

  .pitch { position: absolute; left: 297px; top: 646px; width: 285px; font-size: 12.5px; font-weight: 700; line-height: 1.25; color: #fff; }

  .specials-title { position: absolute; left: 481px; top: 735px; font-family: "Oswald", Impact, sans-serif; font-weight: 500; font-size: 27px; line-height: 0.92; color: var(--orange); }

  .deal { position: absolute; display: flex; align-items: center; justify-content: center; text-align: center; border-radius: 20px; font-weight: 700; line-height: 1.3; }
  .deal--double { left: 290px; top: 774px; width: 184px; height: 134px; background: var(--lime); color: var(--ink); font-size: 16px; }
  .deal--brochure { left: 478px; top: 823px; width: 160px; height: 125px; background: var(--sky); color: var(--ink); font-size: 16px; }
  .deal--package { left: 292px; top: 918px; width: 182px; height: 123px; background: var(--scarlet); color: #fff; font-size: 15px; z-index: 1; }
  .deal--postcards { left: 485px; top: 958px; width: 141px; height: 106px; background: var(--amber); color: var(--ink); font-size: 16px; }
  .deal--flyers { left: 387px; top: 1039px; width: 117px; height: 90px; background: var(--scarlet); color: #fff; font-size: 16px; z-index: 2; border: 2px solid var(--night); }

  .postal-panel { position: absolute; left: 700px; top: 725px; width: 227px; height: 441px; border: 2px solid #fff; border-radius: 20px; }
  .postal-stamp { position: absolute; right: 13px; top: 15px; width: 77px; height: 77px; border: 3px solid var(--red); border-radius: 16px; background: #fff; }
  .postal-label { position: absolute; left: 26px; top: 120px; font-size: 38px; font-weight: 600; line-height: 1.2; color: #fff; }
</style>
</head>
<body>
<main class="postcard">
  <h1 class="headline">Let Us Help Your Business</h1>
  <div class="shine">SHINE !</div>
  <p class="hours">24 hr/ 7day</p>
  <p class="email">orders@cardwillow.com</p>

  <div class="brand"><span class="brand-mark"></span>CardWillow</div>

  <div class="photo photo--dental" role="img" aria-label="Smiling dental receptionist wearing a headset"><span class="photo-tag">Dental</span></div>
  <div class="photo photo--beauty" role="img" aria-label="Beauty portrait of a woman with clear skin"></div>

  <section class="night-band"></section>
  <div class="ghost-words" aria-hidden="true">
    <span style="left:470px;top:2px">banners</span>
    <span style="left:300px;top:140px">booklets</span>
    <span style="left:300px;top:250px">business cards</span>
    <span style="left:520px;top:120px">calendars</span>
    <span style="left:640px;top:140px">catalogs</span>
    <span style="left:300px;top:330px">posters</span>
    <span style="left:560px;top:475px">hangtags</span>
    <span style="left:225px;top:540px">postcards</span>
    <span style="left:520px;top:545px">presentation folders</span>
    <span style="left:400px;top:545px">labels</span>
  </div>

  <div class="photo photo--auto" role="img" aria-label="Front corner of a red sports car with glowing headlight"></div>

  <h2 class="services-title" aria-label="Services"><span>S</span><span>e</span><span>r</span><span>v</span><span>i</span><span>c</span><span>e</span><span>s</span></h2>
  <ul class="service-list">
    <li style="--dot:#8cc63f">banners</li>
    <li style="--dot:#1ba9e6">booklets</li>
    <li style="--dot:#7a4aa0">brochures</li>
    <li style="--dot:#e8308a">business cards</li>
    <li style="--dot:#f7d117">calendars</li>
    <li style="--dot:#1ba9e6">catalogs</li>
    <li style="--dot:#f26522">CD/DVD packages</li>
    <li style="--dot:#f39a1e">envelopes</li>
    <li style="--dot:#e8308a">event tickets</li>
    <li style="--dot:#8cc63f">flyers</li>
    <li style="--dot:#00a99d">hangtags</li>
    <li style="--dot:#1ba9e6">postcards</li>
    <li style="--dot:#1b75bb">posters</li>
    <li style="--dot:#2e3192">presentation folders</li>
    <li style="--dot:#7a4aa0">rackcards</li>
    <li style="--dot:#e6e0c0">labels</li>
  </ul>

  <p class="pitch">Business with no limits, meet mailing with no addresses, gain new customers through "Whole Route Flyer Drop" reach new customers at their home without needing their address.</p>

  <h3 class="specials-title">current<br>specials<br>print</h3>
  <div class="deal deal--double">Double your<br>order FREE<br>(order 500 business<br>cards and get 1000)</div>
  <div class="deal deal--brochure">250 100lb gloss<br>stock<br>brochures 99.00</div>
  <div class="deal deal--package">Business packages<br>(cards, envelopes<br>and letterhead) 299</div>
  <div class="deal deal--postcards">5000 postcards<br>179.99</div>
  <div class="deal deal--flyers">1000 flyers<br>140.40</div>

  <div class="postal-panel">
    <div class="postal-stamp"></div>
    <p class="postal-label">Postal<br>Customer</p>
  </div>
</main>
</body>
</html>
```